Law Firm Website

We are looking to update our old, tired and very flat website. We have someone who will code and host the site but we need some design inspiration. The website will consist of no more than 2/3 pages, possibly with pop-ups for information. We already have all the blurb. We would like something distinctive, clean and eye-catching, using the purple and white theme that we already use on our firm stationery. Examples uploaded. Current website URL is www.holtandbrevis.example.

Industry/Entity Type

Law Firm

```html
<!DOCTYPE html>
<html lang="en">
<head>
<meta charset="utf-8">
<title>Holt + Brevis Solicitors</title>
<link href="https://fonts.googleapis.com/css2?family=Bebas+Neue&family=Carlito:ital,wght@0,400;0,700;1,400&family=Roboto+Slab:wght@300;400&display=swap" rel="stylesheet">
<style>
:root{
  --purple:#564c9e;
  --purple-soft:#6459ab;
  --purple-band:#7569bb;
  --grey-panel:#6c6c6c;
  --page-grey:#e4e4e4;
  --footer:#4b4b4b;
  --gold:#f2b705;
  --logo-green:#1e3a2e;
  --logo-purple:#4a3f8f;
  --white:#ffffff;
}
*{box-sizing:border-box;margin:0;padding:0}
html,body{width:1200px;height:1030px;overflow:hidden}
body{position:relative;background:var(--page-grey);font-family:'Carlito',sans-serif;color:var(--white)}
.hero{position:absolute;left:0;top:0;width:1200px;height:538px;background:linear-gradient(180deg,#5d79b0 0%,#8ea6cf 35%,#cbb89c 60%,#b39f82 100%)}
.site-header{position:absolute;left:0;top:0;width:1200px;height:87px;background:rgba(235,240,250,.78);z-index:2}
.brand{position:absolute;left:190px;top:14px;font-weight:700;line-height:1}
.brand-name{font-size:34px;display:block;color:var(--logo-green)}
.brand-sub{font-size:19px;display:block;margin:6px 0 0 47px;color:var(--logo-purple)}
.main-nav{position:absolute;left:573px;top:0;display:flex;height:87px}
.main-nav a{display:flex;align-items:flex-end;padding:0 15px 20px;font-size:14px;color:#1d1d2b;text-decoration:none}
.main-nav a.active{background:var(--purple);color:var(--white);width:73px;justify-content:center}
.tagline{position:absolute;font-family:'Bebas Neue',sans-serif;font-size:47px;letter-spacing:1px;color:var(--white);background:rgba(25,45,35,.72);padding:0 18px;height:56px;line-height:58px;white-space:nowrap;text-shadow:2px 2px 3px #000;z-index:2}
.tagline.one{left:161px;top:182px}
.tagline.two{left:242px;top:250px}
.panel{position:absolute;z-index:2}
.expertise{left:161px;top:434px;width:448px;height:257px;background:linear-gradient(135deg,var(--purple) 60%,#5e56a6 60%)}
.about{left:609px;top:434px;width:430px;height:257px;background:var(--grey-panel)}
.panel h2{font-family:'Roboto Slab',serif;font-weight:300;font-size:27px;position:absolute;left:22px;top:8px;white-space:nowrap}
.expertise-list{position:absolute;list-style:none;top:62px;font-size:14.5px;line-height:22.3px}
.expertise-list li::before{content:"";display:inline-block;width:10px;height:10px;background:var(--white);margin-right:7px;vertical-align:-1px}
.col-a{left:31px}.col-b{left:230px}
.learn-more{position:absolute;left:304px;top:227px;font-size:12px;color:var(--gold);text-decoration:none;display:flex;align-items:center;gap:5px}
.about-text{position:absolute;left:24px;top:57px;width:400px;font-size:14px;line-height:19px}
.about-text p{margin-bottom:12px}
.about-text a{color:var(--gold);text-decoration:none}
.testimonials{left:161px;top:691px;width:448px;height:240px;background:var(--purple-soft)}
.testimonials h2{left:27px;top:9px}
.quote{position:absolute;left:65px;top:57px;width:345px;font-style:italic;font-size:14.5px;line-height:20.6px}
.quote-mark{font-family:Georgia,serif;font-size:40px;font-weight:700;font-style:normal;color:#dcd8f0;position:absolute;line-height:1}
.quote-open{left:-29px;top:-6px}
.quote-close{right:48px;bottom:-26px}
.quote-author{position:absolute;right:28px;top:186px;font-family:'Roboto Slab',serif;font-size:17px;color:var(--gold);white-space:nowrap}
.partner{position:absolute;top:691px;height:240px;z-index:2}
.partner-one{left:609px;width:173px}
.partner-two{left:782px;width:257px}
.portrait{height:193px}
.partner-one .portrait{background:linear-gradient(180deg,#b8b2a6,#6d6a66)}
.partner-two .portrait{background:linear-gradient(180deg,#2c2c2c,#9a9a9a)}
.partner-name{height:47px;background:var(--purple-band);font-family:'Roboto Slab',serif;font-weight:300;font-size:26px;text-align:center;line-height:47px;white-space:nowrap;color:var(--white)}
.site-footer{position:absolute;left:0;top:896px;width:1200px;height:134px;background:var(--footer);z-index:1}
.badge{position:absolute;left:187px;top:51px;width:173px;height:71px;background:var(--white)}
.footer-links{position:absolute;right:173px;top:58px;font-size:12.5px;font-weight:700}
.footer-links a{color:var(--white);text-decoration:none}
.copyright{position:absolute;right:171px;top:96px;font-size:11.5px;letter-spacing:.8px;color:#d0d0d0}
</style>
</head>
<body>
<div class="hero" role="img" aria-label="Photograph of Gothic court building towers against a blue sky"></div>

<header class="site-header">
  <div class="brand"><span class="brand-name">Holt + Brevis</span><span class="brand-sub">Solicitors</span></div>
  <nav class="main-nav">
    <a class="active" href="#">Home</a>
    <a href="#">Areas of Expertise</a>
    <a href="#">Daniel Holt</a>
    <a href="#">Peter Brevis</a>
    <a href="#">Contact</a>
  </nav>
</header>

<div class="tagline one">Holt &amp; Brevis Solicitors,</div>
<div class="tagline two">For the service you deserve</div>

<section class="panel expertise">
  <h2>Areas of Expertise</h2>
  <ul class="expertise-list col-a">
    <li>Litigation</li><li>Company Matters</li><li>Insolvency</li><li>Corporate and private</li><li>Conveyancing</li><li>Wills &amp; Probate</li><li>Landlord &amp; Tenant</li>
  </ul>
  <ul class="expertise-list col-b">
    <li>Divorce</li><li>Care of the Elderly</li><li>Intellectual Property</li><li>Commercial Crime</li><li>Media Law</li><li>Commercial / Business</li>
  </ul>
  <a class="learn-more" href="#">LEARN MORE
    <svg width="14" height="14" viewBox="0 0 14 14"><circle cx="7" cy="7" r="7" fill="#d9d9e6"/><path d="M3.5 7h6M7 4l3 3-3 3" stroke="#564c9e" stroke-width="1.8" fill="none"/></svg>
  </a>
</section>

<section class="panel about">
  <h2>Holt &amp; Brevis Solicitors</h2>
  <div class="about-text">
    <p>High Court, LondonHOLT and BREVIS is a firm of solicitors with offices in Hampstead, London and Welwyn, Hertfordshire.</p>
    <p style="margin-top:22px">This firm is authorised and regulated by the Legal Practice Standards Board, no.524412.</p>
    <p>VAT registered number: 625 5884 13</p>
    <p>Professional rules can be viewed on<br><a href="#">www.lpsb.example/code-of-conduct.page.</a></p>
  </div>
</section>

<section class="panel testimonials">
  <h2>Client Testimonials</h2>
  <blockquote class="quote">
    <span class="quote-mark quote-open">&ldquo;</span>
    This is Draftline's version &nbsp;of Lorem Ipsum. Proin gravida nibh vel velit auctor aliquet. Aenean sollicitudin, lorem quis bibendum auctor, nisi elit consequat ipsum, nec sagittis sem nibh id elit. Duis sed odio sit amet nibh vulputate cursus a sit amet mauris...
    <span class="quote-mark quote-close">&rdquo;</span>
  </blockquote>
  <div class="quote-author">- Martin Shaw, CA</div>
</section>

<div class="partner partner-one">
  <div class="portrait" role="img" aria-label="Portrait photograph of partner Daniel Holt"></div>
  <div class="partner-name">Daniel Holt</div>
</div>
<div class="partner partner-two">
  <div class="portrait" role="img" aria-label="Black and white portrait photograph of partner Peter Brevis"></div>
  <div class="partner-name">Peter Brevis</div>
</div>

<footer class="site-footer">
  <div class="badge" role="img" aria-label="Family law association membership badge"></div>
  <div class="footer-links"><a href="#">Legal Notices</a> &nbsp;|&nbsp; <a href="#">Privacy Policy</a></div>
  <div class="copyright">Copyright © 2014 &nbsp;Holt &amp; Brevis &nbsp;| All Rights Reserved.</div>
</footer>
</body>
</html>
```